Letterhead Design for Higher Education provider

Company Name: PELV Credentials
Motto: Rigour in Study
Address: Tamble House, Orchard Rise, Fenwick Trade Park, Hollinsby HB4 9LX, United Kingdom
T: +44 (0)20 7946 0382
E: info@pelv-example.org.uk
W: www.pelv-example.org.uk
Legal information: PELV Credentials is incorporated in England & Wales | Company Reg. No. 07315248

Target Market(s)

Higher Education provider

Industry/Entity Type

Education

Font styles to use
Sans Serif

Requirements
Must have
• Company Name, Address, tel, email, web, company legal information.
Nice to have
• motto
Should not have
• should not cover to much of printing areas

```html
<!DOCTYPE html>
<html lang="en">
<head>
<meta charset="utf-8">
<title>PELV Credentials – Letterhead</title>
<link rel="stylesheet" href="https://fonts.googleapis.com/css2?family=Roboto+Condensed:wght@400;700&family=Ubuntu:wght@300;500&display=swap">
<style>
  :root {
    --navy: #2b3a74;
    --motto: #6f7ba9;
    --ink: #151515;
    --paper: #ffffff;
  }
  * { margin: 0; padding: 0; box-sizing: border-box; }
  html, body { width: 848px; height: 1200px; overflow: hidden; background: var(--paper); }
  .letterhead {
    position: relative;
    width: 848px;
    height: 1200px;
    background: var(--paper);
    font-family: "Roboto Condensed", "Arial Narrow", sans-serif;
    color: var(--ink);
  }
  .masthead {
    position: absolute;
    left: 0; top: 0;
    width: 100%;
    height: 112px;
    background: var(--navy);
    box-shadow: 0 3px 6px rgba(0, 0, 0, 0.28);
    display: flex;
    align-items: center;
    justify-content: center;
  }
  .brand-name {
    font-family: "Ubuntu", sans-serif;
    font-weight: 500;
    font-size: 50px;
    letter-spacing: -1px;
    color: var(--paper);
    line-height: 1;
    margin-top: -4px;
  }
  .address {
    position: absolute;
    left: 40px;
    top: 136px;
    font-size: 13.2px;
    line-height: 17.3px;
    font-style: normal;
    white-space: nowrap;
  }
  .motto {
    position: absolute;
    left: 0;
    width: 100%;
    top: 133px;
    text-align: center;
    font-family: "Ubuntu", sans-serif;
    font-weight: 300;
    font-size: 25px;
    color: var(--motto);
  }
  .contact {
    position: absolute;
    right: 40px;
    top: 136px;
    font-size: 13.2px;
    line-height: 17.3px;
    list-style: none;
    white-space: nowrap;
  }
  .contact .label { font-weight: 700; color: var(--navy); }
  .legal-bar {
    position: absolute;
    left: 0; bottom: 0;
    width: 100%;
    height: 32px;
    background: var(--navy);
    color: var(--paper);
    font-size: 14.5px;
    display: flex;
    align-items: center;
    justify-content: center;
  }
</style>
</head>
<body>
<div class="letterhead">
  <header class="masthead">
    <span class="brand-name">pelv</span>
  </header>

  <address class="address">
    Tamble House, Orchard Rise,<br>
    Fenwick Trade Park,<br>
    Hollinsby HB4 9LX,United Kingdom
  </address>

  <p class="motto">Rigour in Study</p>

  <ul class="contact">
    <li><span class="label">[P]</span> +44 (0)20 7946 0382</li>
    <li><span class="label">[E]</span> info@pelv-example.org.uk</li>
    <li><span class="label">[W]</span> www.pelv-example.org.uk</li>
  </ul>

  <footer class="legal-bar">
    PELV Credentials is incorporated in England &amp; Wales | Company Reg. No. 07315248
  </footer>
</div>
</body>
</html>
```